Business Card Design

Motorvane Ledger is an online automotive resource on a national scale specifically targeting lease purchases for new cars. Our Online and app platform allow prospective lease clients to scan a window sticker while at a franchise dealership and instantly receive a lease quote at what we call the sweet spot. Motorvane Ledger offers price transparency during the lease process to allow average people the confidence in the lease process and takes away any fear of the big franchise dealers.
Motorvane ledger allows ordinary lease customers to know they are getting a low price lease and not overpaying. Never overpay again

Industry/Entity Type

Automotive

Contact Information for Business Card

Motorvane Ledger
Martin Sowerby (President of operations)
Phone: 888-247-6031
Cell: 561-384-2706

```html
<!DOCTYPE html>
<html lang="en">
<head>
<meta charset="utf-8">
<title>Motorvane Ledger — Business Card Back</title>
<link rel="stylesheet" href="https://fonts.googleapis.com/css2?family=Montserrat:wght@400;800&display=swap">
<style>
  :root {
    --sky-top: #1f1f21;
    --sky-mid: #34312e;
    --horizon: #4b3a29;
    --ground: #141414;
    --ground-deep: #0d0d0d;
    --accent: #ffd400;
    --ink-light: #ffffff;
  }
  * { margin: 0; padding: 0; box-sizing: border-box; }
  html, body {
    width: 1200px;
    height: 702px;
    overflow: hidden;
    background: var(--ground-deep);
  }
  .card {
    position: relative;
    width: 1200px;
    height: 702px;
    overflow: hidden;
  }
  .road-scene {
    position: absolute;
    inset: 0;
    background:
      radial-gradient(ellipse 340px 260px at 600px 520px, rgba(70,70,70,0.45), rgba(20,20,20,0) 70%),
      linear-gradient(to bottom,
        var(--sky-top) 0px,
        var(--sky-mid) 110px,
        var(--horizon) 200px,
        #2a241e 232px,
        var(--ground) 280px,
        var(--ground-deep) 702px);
  }
  .brand-name {
    position: absolute;
    right: 60px;
    top: 522px;
    font-family: "Montserrat", sans-serif;
    font-weight: 800;
    font-size: 38px;
    line-height: 36px;
    letter-spacing: -0.5px;
    color: var(--ink-light);
    text-transform: uppercase;
    text-align: left;
  }
  .accent-rule {
    position: absolute;
    left: 0;
    top: 625px;
    width: 691px;
    height: 7px;
    background: var(--accent);
  }
  .web-address {
    position: absolute;
    right: 60px;
    top: 610px;
    font-family: "Montserrat", sans-serif;
    font-weight: 400;
    font-size: 29px;
    line-height: 36px;
    letter-spacing: 0.3px;
    color: var(--accent);
  }
</style>
</head>
<body>
  <div class="card">
    <div class="road-scene" role="img" aria-label="Blurred photograph of an empty highway stretching toward a dusky horizon at twilight"></div>
    <div class="brand-name">Motorvane<br>Ledger</div>
    <div class="accent-rule"></div>
    <div class="web-address">www.motorvaneledger.com</div>
  </div>
</body>
</html>
```